Coffee to go business card

Can you make an Orange card please.
our other colours are black chocolate and white for the writing.
If you could make the name and phone number more prominant.

Target Market(s)

People on the go.

Industry/Entity Type

Business

Contact Information for Business Card

Vireo Espresso Bar - coffee to go
Open at the Orange window
Weekdays 5.30am to 2.30pm
Saturdays 7.30am to 2.00pm
Phone orders welcome 58361907
Shop 9 Brindle Court Centre
17 Tallow Street, Brindle COurt, 4937
Serving Fresh Quarzo Espresso
Like us on facebook

Requirements
Must have
• I have attached our logo but not dure if it uploaded correctly?
Nice to have
• see above

```html
<!DOCTYPE html>
<html lang="en">
<head>
<meta charset="utf-8">
<title>Vireo Espresso Bar – Business Card</title>
<link rel="stylesheet" href="https://fonts.googleapis.com/css2?family=Oswald:wght@600&family=Open+Sans:wght@400&display=swap">
<style>
  :root {
    --peach: #fde0c4;
    --ink-black: #111111;
    --chocolate: #6b2f0c;
    --bean-dark: #2e2520;
    --bean-mid: #5a3a26;
    --glow-orange: #ff7a2a;
    --band-top: #ffa56b;
    --band-main: #ff5f00;
    --band-edge: #a83a00;
    --white: #ffffff;
  }
  * { margin: 0; padding: 0; box-sizing: border-box; }
  html, body {
    width: 1200px;
    height: 741px;
    overflow: hidden;
    background: var(--peach);
  }
  .card {
    position: relative;
    width: 1200px;
    height: 741px;
    background: var(--peach);
    font-family: "Open Sans", Arial, sans-serif;
    overflow: hidden;
  }
  .cup-decoration {
    position: absolute;
    left: 162px;
    top: 260px;
    width: 920px;
    height: 280px;
    border-radius: 50%;
    background: radial-gradient(ellipse at center, rgba(214, 180, 150, 0.28) 0%, rgba(214, 180, 150, 0.12) 55%, rgba(214, 180, 150, 0) 75%);
  }
  .beans-illustration {
    position: absolute;
    left: 92px;
    top: 92px;
    width: 184px;
    height: 194px;
    border-radius: 40%;
    background: radial-gradient(circle at 45% 45%, var(--bean-mid) 0%, var(--bean-dark) 70%);
    box-shadow: 0 6px 14px rgba(0, 0, 0, 0.25);
  }
  .business-name {
    position: absolute;
    left: 317px;
    top: 94px;
    font-family: "Oswald", "Arial Narrow", sans-serif;
    font-weight: 600;
    font-size: 152px;
    line-height: 1.2;
    letter-spacing: -1px;
    color: var(--ink-black);
    text-shadow: 0 4px 10px var(--glow-orange);
    white-space: nowrap;
    transform: scaleX(0.64);
    transform-origin: left top;
  }
  .tagline {
    position: absolute;
    left: 0;
    top: 314px;
    width: 1314px;
    text-align: center;
    font-size: 36.5px;
    line-height: 1.2;
    color: var(--chocolate);
    text-shadow: 0 2px 6px var(--glow-orange);
    white-space: nowrap;
  }
  .opening-hours {
    position: absolute;
    left: 390px;
    top: 388px;
    font-size: 36px;
    line-height: 52px;
    color: var(--chocolate);
    text-shadow: 0 2px 6px var(--glow-orange);
    list-style: none;
    white-space: nowrap;
  }
  .order-band {
    position: absolute;
    left: 0;
    top: 549px;
    width: 1200px;
    height: 140px;
    background: linear-gradient(to bottom, var(--band-top) 0%, var(--band-main) 18%, var(--band-main) 88%, var(--band-edge) 100%);
    color: var(--white);
    text-align: center;
    padding-left: 10px;
    padding-top: 22px;
    font-size: 36px;
    line-height: 50px;
  }
  .order-band .order-note { display: block; }
  .order-band .phone-number { display: block; margin-left: -14px; }
</style>
</head>
<body>
  <main class="card">
    <div class="cup-decoration" role="img" aria-label="Faint outline of a coffee cup and saucer behind the text"></div>
    <div class="beans-illustration" role="img" aria-label="Illustration of three roasted coffee beans"></div>

    <h1 class="business-name">Vireo Espresso Bar</h1>
    <p class="tagline">Coffee to go Open at the Orange window</p>

    <ul class="opening-hours">
      <li>Weekdays 5.30am to 2.30pm</li>
      <li>Saturdays 7.30am to 2.00pm</li>
    </ul>

    <section class="order-band">
      <span class="order-note">Phone orders welcome</span>
      <span class="phone-number">58361907</span>
    </section>
  </main>
</body>
</html>
```